Business Card for Industrial Distributor

We need a business card design for an industrial distributor. We sell machine parts for the manufacturing and oil industry. We would like the cards to look clean and modern but with a touch of industry.

Our colors are blue/white.

Please feel free to visit our website www.krovelmint.com

Target Market(s)

mexican manufacturers in the automobile/aerospace industry

Industry/Entity Type

Industrial

Colors
ffffff
0555a3

```html
<!DOCTYPE html>
<html lang="en">
<head>
<meta charset="utf-8">
<title>Krovelmint Business Card</title>
<link href="https://fonts.googleapis.com/css2?family=Ubuntu:wght@400;500;700&display=swap" rel="stylesheet">
<style>
  :root{
    --bg:#d9d9db;
    --navy:#2e2f86;
    --blue:#3b4ba8;
    --blue-light:#4f7fc4;
    --accent:#4a6fc0;
    --white:#ffffff;
    --ink:#3a3a4a;
  }
  *{margin:0;padding:0;box-sizing:border-box}
  html,body{width:1200px;height:990px;overflow:hidden}
  body{background:var(--bg);font-family:"Ubuntu",sans-serif;position:relative}
  .card{position:absolute;top:346px;width:520px;height:297px;border-radius:18px;overflow:hidden;box-shadow:0 6px 14px rgba(0,0,0,.22)}
  .card-front{left:50px;background:var(--white)}
  .card-back{left:630px;background:radial-gradient(circle at 58% 42%,var(--blue-light) 0%,#3f58b0 38%,var(--navy) 78%)}
  .wordmark{display:flex;align-items:center;gap:8px;color:var(--navy);font-weight:700;letter-spacing:-.5px}
  .wordmark .dot{border-radius:50%;background:var(--navy);flex:none}
  .card-front .wordmark{position:absolute;top:40px;right:34px;font-size:34px}
  .card-front .wordmark .dot{width:40px;height:40px}
  .holder{position:absolute;left:32px;top:58px}
  .holder-name{font-weight:700;font-size:16px;color:var(--navy);letter-spacing:.3px;text-transform:uppercase}
  .holder-title{font-size:12px;color:var(--ink);margin-top:1px}
  .contacts{position:absolute;left:32px;top:184px;list-style:none;font-size:12px;color:var(--ink)}
  .contacts li{display:flex;align-items:center;gap:7px;height:17px}
  .contacts svg{width:12px;height:12px;flex:none}
  .address{position:absolute;right:32px;top:200px;text-align:right;font-size:12px;color:var(--ink);line-height:17px}
  .swoosh{position:absolute;left:0;bottom:0;width:520px;height:40px}
  .card-back .logo-block{position:absolute;left:0;right:0;top:112px;display:flex;flex-direction:column;align-items:center}
  .card-back .wordmark{color:var(--white);font-size:44px}
  .card-back .wordmark .dot{width:54px;height:54px;background:var(--white)}
  .card-back .site{color:var(--white);font-size:12px;margin-top:0;padding-left:60px}
</style>
</head>
<body>
  <section class="card card-front">
    <div class="holder">
      <p class="holder-name">Marco Velandri</p>
      <p class="holder-title">General Manager</p>
    </div>
    <div class="wordmark"><span class="dot"></span>Krovelmint</div>
    <ul class="contacts">
      <li><svg viewBox="0 0 12 12"><rect width="12" height="12" rx="2" fill="#2e2f86"/><path d="M3.5 2.5l1.5 0 .6 2-1 .8a5 5 0 0 0 2 2l.8-1 2 .6v1.5c-3.5.5-6.4-2.4-5.9-5.9z" fill="#fff"/></svg>(555) 214-3870</li>
      <li><svg viewBox="0 0 12 12"><rect width="12" height="12" rx="2" fill="#2e2f86"/><rect x="3" y="2" width="6" height="3" fill="#fff"/><rect x="2" y="5.5" width="8" height="4" rx="1" fill="#fff"/></svg>(555) 214-3871</li>
      <li><svg viewBox="0 0 12 12"><rect width="12" height="12" rx="2" fill="#2e2f86"/><rect x="2" y="3.5" width="8" height="5" fill="#fff"/><path d="M2 3.5l4 3 4-3" stroke="#2e2f86" fill="none" stroke-width=".8"/></svg>sales@krovelmint.com</li>
      <li><svg viewBox="0 0 12 12"><rect width="12" height="12" rx="2" fill="#2e2f86"/><circle cx="6" cy="6" r="3.6" fill="none" stroke="#fff" stroke-width=".9"/><path d="M2.4 6h7.2M6 2.4v7.2" stroke="#fff" stroke-width=".8"/></svg>www.krovelmint.com</li>
    </ul>
    <p class="address">4820 Calder Mill Rd.<br>Harlow Bend, TX 70412</p>
    <svg class="swoosh" viewBox="0 0 520 40" preserveAspectRatio="none" aria-hidden="true">
      <path d="M0 22 C150 2 330 0 520 30 L520 40 L0 40Z" fill="var(--accent)"/>
      <path d="M0 30 C170 10 350 8 520 34 L520 40 L0 40Z" fill="#e6e8f2"/>
      <path d="M0 33 C170 14 360 14 520 38 L520 40 L0 40Z" fill="var(--navy)"/>
    </svg>
  </section>

  <section class="card card-back">
    <div class="logo-block">
      <div class="wordmark"><span class="dot"></span>Krovelmint</div>
      <p class="site">www.krovelmint.com</p>
    </div>
  </section>
</body>
</html>
```